Serious, modern business brochure needed for private investigator

Thornbury & Partners Ltd. needs a general brochure that professionally communicates available private investigator services. The brochure will be placed on desks and lobbies. Also, will be carried into offices by hand. The brochure size is left to the designer’s discretion. The brochure needs to communicate high level of professional service provide by Thornbury & Partners and also capture the high risk, fast paced, high stress, environment private investigators work in.

Industry/Entity Type

Business

Requirements
Must have
• Include provided text content
• Include Thornbury & Partners logo

```html
<!DOCTYPE html>
<html lang="en">
<head>
<meta charset="utf-8">
<title>Thornbury &amp; Partners Ltd. — Brochure</title>
<link rel="stylesheet" href="https://fonts.googleapis.com/css2?family=Open+Sans:wght@300;400;600&display=swap">
<style>
  :root {
    --backdrop: #e6e4e1;
    --paper: #ffffff;
    --ink: #1f1f1f;
    --body-ink: #2c2c2c;
    --panel: #333333;
    --footer: #1c1c1c;
    --on-dark: #f1f1f1;
    --photo-light: #c9c9c9;
    --photo-mid: #8a8a8a;
    --photo-dark: #2e2e2e;
  }
  * { margin: 0; padding: 0; box-sizing: border-box; }
  html, body { width: 1200px; height: 728px; overflow: hidden; }
  body {
    background: var(--backdrop);
    font-family: "Open Sans", Arial, sans-serif;
    color: var(--ink);
    position: relative;
  }
  .page {
    position: absolute;
    top: 48px;
    width: 450px;
    height: 635px;
    background: var(--paper);
    box-shadow: 0 4px 14px rgba(0,0,0,0.22);
    overflow: hidden;
  }
  .page--cover { left: 75px; }
  .page--services { left: 674px; }

  /* Cover */
  .cover-title {
    position: absolute;
    left: 50px;
    top: 480px;
    transform: rotate(-90deg);
    transform-origin: left top;
    font-size: 35px;
    font-weight: 400;
    letter-spacing: 0.6px;
    white-space: nowrap;
    line-height: 1;
  }
  .cover-tagline {
    position: absolute;
    left: 116px;
    top: 312px;
    transform: rotate(-90deg);
    transform-origin: left top;
    font-size: 15.5px;
    font-weight: 300;
    white-space: nowrap;
    line-height: 1;
  }
  .photo {
    position: absolute;
    top: 344px;
    height: 222px;
  }
  .photo--strip {
    left: 0; width: 31px;
    background: linear-gradient(180deg, var(--photo-mid), var(--photo-light) 55%, var(--photo-mid));
  }
  .photo--scene {
    left: 117px; width: 333px;
    background: radial-gradient(ellipse at 55% 60%, #f2f2f2 0%, var(--photo-light) 25%, var(--photo-mid) 60%, var(--photo-dark) 100%);
  }
  .brand-mark {
    position: absolute;
    left: 0; top: 566px;
    width: 117px; height: 69px;
    display: flex; align-items: center; justify-content: center;
    text-align: center;
    font-size: 10px;
    font-weight: 600;
    color: var(--ink);
    line-height: 1.25;
    padding: 0 10px;
  }
  .cover-contact {
    position: absolute;
    left: 117px; top: 566px;
    width: 333px; height: 69px;
    background: var(--footer);
    color: var(--on-dark);
    font-size: 8.6px;
    font-weight: 400;
    text-align: center;
    white-space: nowrap;
    padding-top: 20px;
    line-height: 1.4;
  }

  /* Services */
  .service {
    position: absolute;
    left: 31px;
    width: 392px;
  }
  .service h2 {
    font-size: 15.5px;
    font-weight: 400;
    line-height: 1.2;
    margin-bottom: 2px;
  }
  .service p {
    font-size: 8.1px;
    line-height: 1.45;
    color: var(--body-ink);
  }
  .service--criminal { top: 29px; }
  .service--civil { top: 143px; }
  .service--forensic { top: 244px; }

  .info-panel {
    position: absolute;
    left: 0; top: 344px;
    width: 450px; height: 222px;
    background: var(--panel);
  }
  .info-panel .photo--edge {
    position: absolute;
    right: 0; top: 0;
    width: 26px; height: 222px;
    background: linear-gradient(180deg, #555, #8e8e8e 50%, #555);
  }
  .service--info { top: 17px; color: var(--on-dark); }
  .service--info h2 { margin-bottom: 22px; }
  .service--info p { color: var(--on-dark); }

  .promise {
    position: absolute;
    left: 0; top: 566px;
    width: 450px; height: 56px;
    display: flex; align-items: center; justify-content: center;
    gap: 12px;
  }
  .promise p {
    font-size: 8.8px;
    line-height: 1.4;
    text-align: center;
    color: var(--body-ink);
  }
  .page-band {
    position: absolute;
    left: 0; bottom: 0;
    width: 450px; height: 13px;
    background: var(--footer);
  }
</style>
</head>
<body>

<section class="page page--cover">
  <h1 class="cover-title">Thornbury &amp; Partners Ltd.</h1>
  <p class="cover-tagline">A Private Investigation and Analysis Firm</p>
  <div class="photo photo--strip" role="img" aria-label="Edge of a misty black and white forest"></div>
  <div class="photo photo--scene" role="img" aria-label="Black and white misty forest with a lone investigator holding a flashlight between tall trees"></div>
  <div class="brand-mark">Thornbury &amp; Partners</div>
  <div class="cover-contact">
    info@thornburypi.com 1-888-555-0142 P.O. Box 214 Millbrook, Ohio 45600<br>
    thornburypi.com
  </div>
</section>

<section class="page page--services">
  <article class="service service--criminal">
    <h2>Criminal Defense Investigation</h2>
    <p>We specialize in criminal defense investigations. We have a proven ability to find evidence that has been overlooked or ignored by law enforcement. Thornbury &amp; Partners investigators are experts at identifying unknown witnesses, finding physical evidence, and testing the credibility of criminal allegations brought against a defendant. We use a variety of proven investigative methods including field investigation and advanced analytical techniques. All cases are billed at a flat rate, so you know the exact cost of your investigation. Private and indigent defense cases are accepted.</p>
  </article>

  <article class="service service--civil">
    <h2>Civil Investigation</h2>
    <p>Thornbury &amp; Partners provides customized investigative support in civil matters. We are able to investigate a full range of issues such as child custody, worker’s compensation, slip and trips, general accidents, and many other matters. We provide specific investigative tasks involving surveillance, locating persons, witness interviews, asset identification, process service, and courthouse record searches. Most investigations are billed at a flat rate, so you know your cost up front.</p>
  </article>

  <article class="service service--forensic">
    <h2>Forensic Photography</h2>
    <p>Thornbury &amp; Partners provides forensic photography services. We are able to document physical objects, locations, and individuals through accepted photography methods. Not only do we capture images for your use in court, but we are available to provide expert testimony on the image process and the images’ reasonable representation of what was viewed by the photographer. All forensic photography services include images in a digital medium, a written report, a photography log, and a diagram if appropriate.</p>
  </article>

  <div class="info-panel">
    <div class="photo--edge" role="img" aria-label="Edge of a misty black and white forest"></div>
    <article class="service service--info">
      <h2>Information Services</h2>
      <p>Do you need information on someone? Are you completing your own investigation instead of hiring a licensed investigator? Do you need something simple like a phone number or address but find that Searchly can’t help you? Thornbury &amp; Partners is able to assist you by providing information on the person you are investigating. We use tools and proprietary databases that only licensed investigators can access. Thornbury &amp; Partners provides this information to the general public through our Public Inquiry service. See thornburypi.com/store to browse our services.</p>
    </article>
  </div>

  <div class="promise">
    <svg width="20" height="20" viewBox="0 0 20 20" aria-hidden="true">
      <circle cx="8" cy="8" r="5.6" fill="none" stroke="#111" stroke-width="2.6"/>
      <line x1="12.2" y1="12.2" x2="18" y2="18" stroke="#111" stroke-width="3" stroke-linecap="round"/>
    </svg>
    <p>Competitive fees for investigative services<br>In-your-face, objective information</p>
  </div>
  <div class="page-band"></div>
</section>

</body>
</html>
```